Book Cover Design Project - SIMPLE ART, Pre-Concepted

We already have a full design concept for the cover art. It is however in a low quality word document format. This project is to recreate existing example guideline art in as much vector art possible for great quality print production. Artistic flare is welcome. This will be for a book cover (front/back) and I want the quality to be excellent.

Art to be provided in Adobe Illustrator format. The book will be 6wide x 9high, so the artboard for the cover needs to be set up to 12.5 wide x 9 high with .125" bleeds.

Copy content for the spine: "Beneath a Copper Evening Sky Still" RL Moskowicz.

Here is a link to download the word document "template" and a new photo for the back page. I'm not sure that I like the new photo, it is possible the old one in the word document will work.

www.bluemarlinpressworks.com/uploads/QuillHavenSharedFiles.zip

I've got a fast deadline on this project because the client would like to have manufacturing completed by Christmas...which is why this is only a 2 day project. I appreciate your interest in our project.

Gordon

Try this link...seems I was missing the .zip extension which may have been causing problems.

Requirements
Must have
• Adobe Illustrator Files
CMYK color setup - no color definitions for project
Artboard Size: 12.625 wide x 9.125 high
Art Orientation: Flat image should have the back book page on the left side, front page on the right side, spine copy running down the middle.

```html
<!DOCTYPE html>
<html lang="en">
<head>
<meta charset="utf-8">
<title>Beneath a Copper Evening Sky Still — Cover Spread</title>
<link rel="stylesheet" href="https://fonts.googleapis.com/css2?family=Alegreya+Sans+SC:wght@500;700;800&display=swap">
<style>
  :root {
    --paper: #ffffff;
    --ink: #111111;
    --spine: #000000;
    --cross: #050505;
    --cross-edge: #6b6b6b;
    --light: #ffffff;
    --photo-tone: #8e8e8e;
  }
  * { margin: 0; padding: 0; box-sizing: border-box; }
  html, body { width: 1200px; height: 425px; overflow: hidden; background: var(--paper); }
  .spread {
    position: relative;
    width: 1200px;
    height: 425px;
    font-family: "Alegreya Sans SC", "Trebuchet MS", sans-serif;
    color: var(--ink);
    overflow: hidden;
  }

  /* Back cover */
  .back-cover { position: absolute; left: 0; top: 0; width: 565px; height: 425px; background: var(--paper); }
  .author-photo {
    position: absolute; left: 62px; top: 52px; width: 110px; height: 138px;
    background: linear-gradient(180deg, #cfcfcf 0%, #a5a5a5 45%, #3a3a3a 100%);
    border: 1px solid #bdbdbd;
    transform: rotate(2deg);
    box-shadow: 1px 1px 2px rgba(0,0,0,.25);
  }
  .about {
    position: absolute; left: 232px; top: 66px; width: 304px;
    font-weight: 500;
  }
  .about-lead { font-size: 9.5px; line-height: 12.5px; font-weight: 700; }
  .about-lead strong { font-weight: 800; }
  .about-verse { font-size: 9.5px; font-weight: 700; margin-top: 11px; }
  .about-body {
    font-size: 6.4px; line-height: 9.3px; text-align: justify;
    margin-top: 16px; letter-spacing: .05px;
  }
  .about-body + .about-body { margin-top: 9px; }

  /* Spine */
  .spine {
    position: absolute; left: 565px; top: 0; width: 35px; height: 425px;
    background: var(--spine);
  }
  .spine-copy {
    position: absolute; left: 50%; top: 212px;
    transform: translate(-50%, -50%) rotate(90deg);
    white-space: nowrap; color: var(--light);
    font-size: 10px; font-weight: 700; letter-spacing: .3px;
  }

  /* Front cover */
  .front-cover { position: absolute; left: 600px; top: 0; width: 600px; height: 425px; }
  .sky {
    position: absolute; inset: 0;
    background:
      radial-gradient(ellipse 170px 130px at 470px 210px, rgba(255,255,255,.95), rgba(255,255,255,0) 75%),
      radial-gradient(ellipse 260px 90px at 520px 40px, rgba(230,230,230,.9), rgba(230,230,230,0) 80%),
      radial-gradient(ellipse 230px 150px at 130px 90px, rgba(20,20,20,.9), rgba(20,20,20,0) 80%),
      radial-gradient(ellipse 200px 110px at 160px 330px, rgba(150,150,150,.6), rgba(150,150,150,0) 80%),
      linear-gradient(100deg, #2b2b2b 0%, #4a4a4a 30%, #8a8a8a 55%, #d6d6d6 80%, #f2f2f2 100%);
  }
  .cross { position: absolute; left: 0; top: 0; }
  .title {
    position: absolute; left: 405px; top: 247px;
    color: var(--light); font-size: 15px; line-height: 21px; font-weight: 700;
    letter-spacing: .6px;
  }
  .credit {
    position: absolute; left: 405px; top: 377px;
    color: var(--light); font-size: 7.2px; font-weight: 700; letter-spacing: .2px;
  }
</style>
</head>
<body>
<main class="spread">
  <section class="back-cover">
    <div class="author-photo" role="img" aria-label="Portrait photograph of the author in a dark suit and striped tie"></div>
    <article class="about">
      <p class="about-lead"><strong>About the author:</strong> The word of God says that "I know the plans I have for you" (Jeremiah 29:11) and that "before I formed you in the womb I knew you" (Jeremiah 1:15).</p>
      <p class="about-verse">These verses of scripture depict the life of Raymond L Moskowicz.</p>
      <p class="about-body">As a little boy Raymond was always told that he was going to be a preacher. The magnitude of this repeated statement and exactly what it entailed was not taken seriously or truly understood, at that time. It was not Raymond's plan or desire to be a preacher, and he tried to do anything and everything to avoid the talks of him becoming one. Raymond's path of life, although he believed in God, took him down the road that led him away from God. His struggles with life's events and being an introvert kept him emotionally troubled, in a state of depression and wanting to commit suicide. Yet, as the Lord was with Jeremiah, even so was the Lord with Raymond. The Lord was to show Raymond just what it meant to have complete trust in Him and to know that He would always provide a way of an escape. Before Raymond came to the point of carrying out his plans to commit suicide, he prayed a simple prayer that God would give him a new family. At that exact moment Raymond's life began to take a new direction. He began to seek after the Lord; it became his quest to find out what it meant to be a servant of God. Because of his being an introvert, he began to write his emotions on paper in the form of poems. Those poems gave him the strength to come out of depression and began his two year journey to find God.</p>
      <p class="about-body">Raymond's relationship with Jesus and salvation journey began at the age of nineteen. The poetry writing started as a therapeutic remedy for his troubled past, but developed into the psalms of Raymond because of God's grace and mercy that delivered him from despair and hopelessness.</p>
      <p class="about-body">God's favor covers Raymond's life and carries him from day to day. It is written that "without me (Christ) ye can do nothing" (John 15:5). This scripture resonates in Raymond's heart. For, he truly believes that God is the author and he is just the vessel used of God. His desire is that each poem will be taken personally and become a tool used by everyone to help them on their Christian journey and to let them know that they are never alone in their experience and quest to be closer to the Lord Jesus Christ.</p>
    </article>
  </section>

  <aside class="spine">
    <p class="spine-copy">"Beneath a Copper Evening Sky Still" RL Moskowicz</p>
  </aside>

  <section class="front-cover">
    <div class="sky" role="img" aria-label="Black and white photograph of a dramatic cloudy sky with sun rays breaking through"></div>
    <svg class="cross" width="600" height="425" viewBox="0 0 600 425" aria-hidden="true">
      <rect x="258" y="36" width="54" height="352" rx="8" fill="var(--cross-edge)"/>
      <rect x="208" y="127" width="196" height="36" rx="8" fill="var(--cross-edge)"/>
      <rect x="258" y="33" width="54" height="350" rx="8" fill="var(--cross)"/>
      <rect x="208" y="124" width="196" height="34" rx="8" fill="var(--cross)"/>
    </svg>
    <h1 class="title">Beneath a Copper<br>Evening Sky<br>Still</h1>
    <p class="credit">A compilation of poems by RL Moskowicz</p>
  </section>
</main>
</body>
</html>
```